Design a styled business card for an intimacy and attachment psychologist

I am a Psychologist providing online therapy to patients across the United States. My work is interpersonal and emotion-focused, with an emphasis on the client-therapist relationship. My primary areas of work are very personal, including sexuality and gender, abuse and trauma, and grief and loss. My target audience will be adults of all ages 18+.
My business card should convey a warm and inviting feeling of professionalism that is also casual and comfortable.
The front should be fairly simple and professional, consisting of:
- My name, Dr. Rosalind Petrakis
- My title, Licensed Psycholigist
- My logo
On either the front or the back, my contact information should be listed:
- ros@drrospetrakis.example
- 555.014.7788
- drrospetrakis.example
On the rear, I would like a description of the areas that I specialize in. This can be formatted in any way that appears stylistically interesting.
Individual and Couples
Relationships and Infidelity
Sexual Health & Aging
Gender Identity & Sexual Orientation
Abuse and Trauma
Sexual Compulsivity & Addiction
Sexual Dysfunction
Target Market(s)
My target audience will be adults of all ages 18+.
Industry/Entity Type
Psychology
Contact Information for Business Card
The front should be fairly simple and professional, consisting of: - My name, Dr. Rosalind Petrakis - My title, Licensed Psycholigist - My logo On either the front or the back, my contact information should be listed: - ros@drrospetrakis.example - 555.014.7788 - drrospetrakis.example On the rear, I would like a description of the areas that I specialize in. This can be formatted in any way that appears stylistically interesting. Individual and Couples Relationships and Infidelity Sexual Health & Aging Gender Identity & Sexual Orientation Abuse and Trauma Sexual Compulsivity & Addiction Sexual Dysfunction
- Follow brand guide

```html
<!DOCTYPE html>
<html lang="en">
<head>
<meta charset="utf-8">
<title>Dr. Rosalind Petrakis – Business Card</title>
<link rel="stylesheet" href="https://fonts.googleapis.com/css2?family=Montserrat:wght@400;500;600;700&display=swap">
<style>
  :root {
    --bg: #d9d9dc;
    --card-white: #fcfcfc;
    --card-grey: #ececee;
    --navy: #262046;
    --navy-soft: #5f5878;
    --purple: #9a62a8;
    --purple-light: #a97bb5;
    --ink: #2c2750;
    --text-light: #f2f0f6;
    --mark: #7fcdb5;
  }
  * { box-sizing: border-box; margin: 0; padding: 0; }
  html, body { width: 1200px; height: 1200px; overflow: hidden; }
  body {
    background: var(--bg);
    font-family: "Montserrat", sans-serif;
    position: relative;
  }
  .card {
    position: absolute;
    left: 180px;
    width: 840px;
    height: 480px;
    border-radius: 26px;
    overflow: hidden;
    box-shadow: 0 10px 28px rgba(0,0,0,0.18);
  }
  .card--front { top: 100px; background: var(--card-white); }
  .card--back { top: 620px; background: var(--card-grey); }

  .brand {
    display: flex;
    align-items: center;
    gap: 24px;
    position: absolute;
  }
  .brand__dot {
    border-radius: 50%;
    background: var(--mark);
    border: 5px solid var(--ink);
    flex: none;
  }
  .brand__name {
    color: var(--ink);
    font-weight: 600;
    text-transform: uppercase;
    letter-spacing: 0.04em;
    line-height: 1.05;
  }
  .card--front .brand { left: 50%; top: 50%; transform: translate(-50%, -50%); }
  .card--front .brand__dot { width: 140px; height: 140px; }
  .card--front .brand__name { font-size: 46px; }

  .card--back .brand { right: 60px; top: 42px; gap: 18px; }
  .card--back .brand__dot { width: 92px; height: 92px; border-width: 4px; }
  .card--back .brand__name { font-size: 30px; }

  .back-shape { position: absolute; inset: 0; width: 100%; height: 100%; }

  .contact {
    position: absolute;
    left: 60px;
    bottom: 48px;
    color: var(--text-light);
  }
  .contact__name { color: var(--purple-light); font-weight: 700; font-size: 28px; }
  .contact__title { font-size: 19px; margin-top: 4px; margin-bottom: 26px; }
  .contact__list { list-style: none; font-size: 19px; }
  .contact__list li { display: flex; align-items: center; gap: 14px; margin-top: 6px; }
  .contact__list svg { width: 18px; height: 18px; flex: none; }

  .address {
    position: absolute;
    right: 60px;
    bottom: 150px;
    color: var(--text-light);
    font-size: 19px;
    line-height: 1.45;
  }
</style>
</head>
<body>
  <section class="card card--front">
    <div class="brand">
      <span class="brand__dot"></span>
      <span class="brand__name">Dr.<br>Rosalind<br>Petrakis</span>
    </div>
  </section>

  <section class="card card--back">
    <svg class="back-shape" viewBox="0 0 840 480" preserveAspectRatio="none" aria-hidden="true">
      <defs>
        <linearGradient id="navyFade" x1="0" y1="0" x2="1" y2="0.4">
          <stop offset="0" stop-color="#615a7b"/>
          <stop offset="0.45" stop-color="#2c2549"/>
          <stop offset="1" stop-color="#262046"/>
        </linearGradient>
      </defs>
      <path d="M0,0 L120,0 C300,120 450,255 570,262 C690,268 790,215 840,150 L840,480 L0,480 Z" fill="url(#navyFade)"/>
      <path d="M150,0 L190,0 C340,110 470,240 600,258 C520,262 440,220 360,160 C290,110 220,55 150,0 Z" fill="var(--purple)"/>
    </svg>

    <div class="brand">
      <span class="brand__dot"></span>
      <span class="brand__name">Dr.<br>Rosalind<br>Petrakis</span>
    </div>

    <div class="contact">
      <p class="contact__name">Dr. Rosalind Petrakis</p>
      <p class="contact__title">Licensed Psycholigist</p>
      <ul class="contact__list">
        <li>
          <svg viewBox="0 0 24 24" fill="var(--purple)"><path d="M6.6 10.8a15.1 15.1 0 0 0 6.6 6.6l2.2-2.2a1 1 0 0 1 1-.25 11.4 11.4 0 0 0 3.6.57 1 1 0 0 1 1 1V20a1 1 0 0 1-1 1A17 17 0 0 1 3 4a1 1 0 0 1 1-1h3.5a1 1 0 0 1 1 1c0 1.25.2 2.45.57 3.57a1 1 0 0 1-.25 1z"/></svg>
          555.014.7788
        </li>
        <li>
          <svg viewBox="0 0 24 24" fill="var(--purple)"><path d="M2 5h20v14H2z M2 5l10 8 10-8" stroke="var(--navy)" stroke-width="1.5"/></svg>
          ros@drrospetrakis.example
        </li>
        <li>
          <svg viewBox="0 0 24 24" fill="none" stroke="var(--purple)" stroke-width="2.2"><circle cx="12" cy="12" r="9"/><path d="M3 12h18M12 3c3 3.5 3 14.5 0 18M12 3c-3 3.5-3 14.5 0 18"/></svg>
          www.drrospetrakis.example
        </li>
      </ul>
    </div>

    <p class="address">4180 Alder Lane<br>Harbor Falls Maine 04011</p>
  </section>
</body>
</html>
```